Non-profit needs fresh graphics for online fundraiser.

We are wanting some fresh, spring-themed graphics for our spring online auction fundraiser. We are a faith based non-profit that serves families who have a child facing a devastating medical crisis. The design we go with will be used for multiple things...banners, VM posts, auction website etc...

Target Market(s)

These will be used for social media advertising, email marketing, and on our custom auction website.

Industry/Entity Type

Non-Profit

Font styles to use
Decorative
Script

Requirements
Must have
• This title: TAVI's Foundation Spring Online Auction or TAVI's Foundation Spring Petal Parade
Nice to have
• Maybe include our logo but not as the centerpiece. Possibly some flowers or watercolor effects but hoping to see ideas beyond these parameters also.
Should not have
• Dark colors

```html
<!DOCTYPE html>
<html lang="en">
<head>
<meta charset="UTF-8">
<title>TAVI's Foundation Spring Petal Parade</title>
<link rel="stylesheet" href="https://fonts.googleapis.com/css2?family=Poppins:wght@600&family=Oswald:wght@600;700&display=swap">
<style>
  :root {
    --frame-pink: #f6a3f3;
    --paper: #ffffff;
    --ink-shadow: #520a4f;
    --splash-violet: #8a2be2;
    --splash-magenta: #e35bf0;
    --splash-pink: #fb9cf6;
    --splash-soft: #fcc3fb;
  }
  html, body {
    margin: 0;
    padding: 0;
    width: 1200px;
    height: 960px;
    overflow: hidden;
    background: var(--paper);
  }
  .poster {
    position: absolute;
    left: 49px;
    top: 78px;
    width: 1091px;
    height: 803px;
    background: var(--frame-pink);
    box-shadow: 4px 10px 18px rgba(0,0,0,0.55);
  }
  .poster__gap {
    position: absolute;
    inset: 16px;
    background: var(--paper);
  }
  .poster__rule {
    position: absolute;
    left: 25px;
    top: 28px;
    right: 25px;
    bottom: 28px;
    border: 14px solid var(--frame-pink);
    background: var(--paper);
  }
  .splash {
    position: absolute;
    left: 57px;
    top: 61px;
    width: 988px;
    height: 689px;
  }
  .title {
    position: absolute;
    left: 0;
    width: 1200px;
    margin: 0;
    color: var(--paper);
    text-align: center;
    line-height: 1;
    white-space: nowrap;
  }
  .title__name {
    top: 330px;
    left: -10px;
    font-family: "Poppins", sans-serif;
    font-weight: 600;
    font-size: 168px;
    letter-spacing: 2px;
    text-shadow: 6px 5px 0 var(--ink-shadow);
  }
  .title__line {
    top: 485px;
    left: -4px;
    font-family: "Oswald", sans-serif;
    font-weight: 600;
    font-size: 84px;
    letter-spacing: 1px;
    text-shadow: 4px 4px 0 var(--ink-shadow);
  }
  .title__event {
    top: 568px;
    left: -6px;
    font-family: "Oswald", sans-serif;
    font-weight: 700;
    font-size: 112px;
    letter-spacing: -1px;
    text-shadow: 5px 5px 0 var(--ink-shadow);
  }
</style>
</head>
<body>
  <div class="poster">
    <div class="poster__gap"></div>
    <div class="poster__rule">
      <svg class="splash" viewBox="0 0 988 689" role="img" aria-label="Watercolour paint splash in violet, magenta and pink tones">
        <defs>
          <radialGradient id="splashTone" cx="0.52" cy="0.46" r="0.6">
            <stop offset="0" stop-color="var(--splash-violet)"/>
            <stop offset="0.4" stop-color="var(--splash-magenta)"/>
            <stop offset="0.75" stop-color="var(--splash-pink)"/>
            <stop offset="1" stop-color="var(--splash-soft)"/>
          </radialGradient>
        </defs>
        <path fill="url(#splashTone)" d="M470 20 C560 0 640 40 700 80 C780 110 860 150 900 230 C960 280 990 360 940 420 C900 480 870 540 780 570 C700 640 600 680 500 640 C420 670 330 650 260 600 C180 640 110 610 90 540 C40 480 0 400 60 340 C80 260 150 200 220 170 C300 110 380 40 470 20 Z"/>
      </svg>
    </div>
  </div>

  <h1 class="title title__name">TAVI'S</h1>
  <p class="title title__line">Foundation Spring</p>
  <p class="title title__event">Petal Parade</p>
</body>
</html>
```